Harold Brisk Mechanical business cards

We need business cards designed for "Harold Brisk Mechanical" "Mechanical & Electrical Contractors" "Specializing in Service & Installation"
"Cooling, Heating, Service, Installations, Residential, Commercial"

```html
<!DOCTYPE html>
<html lang="en">
<head>
<meta charset="utf-8">
<title>Harold Brisk Mechanical – Business Cards</title>
<link href="https://fonts.googleapis.com/css2?family=Open+Sans:wght@400;600;700&family=Roboto:wght@400;500&family=Cabin:wght@600;700&display=swap" rel="stylesheet">
<style>
  :root {
    --backdrop: #5b5b5b;
    --brand-red: #ec1c24;
    --card-white: #ffffff;
    --card-black: #000000;
    --ink-grey: #333333;
    --rule-grey: #262626;
  }
  html, body {
    margin: 0;
    padding: 0;
    width: 1200px;
    height: 802px;
    overflow: hidden;
    background: var(--backdrop);
  }
  .canvas {
    position: relative;
    width: 1200px;
    height: 802px;
  }
  .card {
    position: absolute;
    top: 274px;
    width: 442px;
    height: 265px;
    overflow: hidden;
  }
  .card-front { left: 136px; background: var(--card-white); }
  .card-back  { left: 624px; background: var(--card-black); color: #fff; }

  .front-band { position: absolute; inset: 0; }

  .holder-name {
    position: absolute; left: 0; right: 0; top: 52px;
    text-align: center;
    font: 700 15px/1 "Open Sans", sans-serif;
    color: var(--brand-red);
    letter-spacing: 0.2px;
  }
  .holder-title {
    position: absolute; left: 0; right: 0; top: 71px;
    text-align: center;
    font: 400 12.5px/1 "Roboto", sans-serif;
    color: var(--ink-grey);
  }
  .contact-list {
    position: absolute; left: 24px; top: 111px;
    margin: 0; padding: 0; list-style: none;
    font: 400 12.5px/15.8px "Roboto", sans-serif;
    color: #fff;
  }
  .contact-list li { display: flex; align-items: center; gap: 4px; }
  .contact-list svg { width: 10px; height: 10px; fill: #fff; flex: none; }
  .address {
    position: absolute; left: 24px; top: 180px;
    font: 400 12.5px/16px "Open Sans", sans-serif;
    color: #fff;
  }
  .front-wordmark {
    position: absolute; left: 236px; top: 128px; width: 196px;
    text-align: center;
    font: 700 31px/1 "Open Sans", sans-serif;
    color: #fff;
    letter-spacing: 0.5px;
  }

  .back-mark {
    position: absolute; left: 196px; top: 58px;
    width: 46px; height: 46px;
    background: var(--brand-red);
  }
  .company-name {
    position: absolute; left: 0; right: 0; top: 118px;
    text-align: center;
    font: 700 23px/1.05 "Cabin", sans-serif;
    letter-spacing: 1px;
    color: #fff;
  }
  .company-tagline {
    position: absolute; left: 0; right: 0; top: 177px;
    text-align: center;
    font: 600 12.5px/1 "Open Sans", sans-serif;
    color: #fff;
  }
  .back-rule {
    position: absolute; left: 104px; width: 234px; top: 200px;
    height: 1px; background: var(--rule-grey);
  }
  .services-heading {
    position: absolute; left: 0; right: 0; top: 212px;
    text-align: center;
    font: 500 12.5px/1 "Roboto", sans-serif;
    color: #fff;
  }
  .services-list {
    position: absolute; left: 0; right: 0; top: 228px;
    text-align: center;
    font: 400 12.5px/1 "Roboto", sans-serif;
    color: #fff;
  }
</style>
</head>
<body>
<main class="canvas">

  <section class="card card-front" aria-label="Business card front">
    <svg class="front-band" viewBox="0 0 442 265" aria-hidden="true">
      <polygon points="12,75 217,121 425,61 442,221 229,244 0,227" fill="var(--brand-red)"/>
    </svg>
    <div class="holder-name">MARCUS DELANE</div>
    <div class="holder-title">Managing Director</div>
    <ul class="contact-list">
      <li><svg viewBox="0 0 10 10"><path d="M1 3.5C1 2 2.5 1 5 1s4 1 4 2.5L7.5 4.2 7 3H3L2.5 4.2zM2.5 5h5L9 9H1z"/></svg>055-210 384 617</li>
      <li><svg viewBox="0 0 10 10"><path d="M2.5 0h5a.8.8 0 0 1 .8.8v8.4a.8.8 0 0 1-.8.8h-5a.8.8 0 0 1-.8-.8V.8A.8.8 0 0 1 2.5 0zm.6 1.2v6.6h3.8V1.2zM5 8.3a.5.5 0 1 0 0 1 .5.5 0 0 0 0-1z"/></svg>055-210 384 617</li>
      <li><svg viewBox="0 0 10 10"><path d="M0 2h10v6H0zm1 .8L5 5.6l4-2.8v-.2H1z" fill-rule="evenodd"/></svg>info@hbrisk-mech.com</li>
      <li><svg viewBox="0 0 10 10"><circle cx="5" cy="5" r="4.6"/></svg>www.hbrisk-mech.com</li>
    </ul>
    <div class="address">48 Foundry Lane<br>Eastvale, 204518.</div>
    <div class="front-wordmark">HAROLD<br>BRISK</div>
  </section>

  <section class="card card-back" aria-label="Business card back">
    <div class="back-mark" aria-hidden="true"></div>
    <div class="company-name">HAROLD BRISK<br>MECHANICAL</div>
    <div class="company-tagline">Mechanical &amp; Electrical Contractors</div>
    <div class="back-rule" aria-hidden="true"></div>
    <div class="services-heading">SPECIALIZING IN SERVICE &amp; INSTALLATION</div>
    <div class="services-list">Cooling | Heating | Service | Installations | Residential | Commercial</div>
  </section>

</main>
</body>
</html>
```